TRELLWICK Construction Group business card for distribution

A business card detailing our services, with our phone number and email address.
- Groundworks / Foundations / Drainage
- Landscaping / Hard Landscaping / Patios / Decking
- Fencing
The card should include company logo and be in the same colours.

Target Market(s)
Domestic Houses
Industry/Entity Type
Construction
Contact Information for Business Card
Phone Number - 07931 258 904 / 07713829516. Email address: trellgroup@stonevane-mail.com
Font styles to use
Serif
Sans Serif
Colors
F0912C
F2A743
F7CA91
FBE8D2
FDF5EE
Requirements
Must have
- Contact numbers. Photos of past work. Company Logo

Nice to have
- Company Logo

```html
<!DOCTYPE html>
<html lang="en">
<head>
<meta charset="UTF-8">
<title>TRELLWICK Construction Group – Business Card</title>
<link href="https://fonts.googleapis.com/css2?family=Archivo:wght@400;800&family=Montserrat:wght@400;500;600;800&display=swap" rel="stylesheet">
<style>
  :root {
    --page-bg: #2a2a2b;
    --card-black: #050505;
    --orange: #f0912c;
    --orange-soft: #f2a743;
    --white: #ffffff;
    --grey-text: #e4e4e4;
  }
  * { box-sizing: border-box; margin: 0; padding: 0; }
  html, body {
    width: 1200px; height: 689px; overflow: hidden;
    background: var(--page-bg);
  }
  .sheet {
    width: 1200px; height: 689px;
    display: flex; align-items: center; justify-content: center; gap: 40px;
  }
  .card {
    position: relative;
    width: 540px; height: 309px;
    background: var(--card-black);
    border-radius: 18px;
    overflow: hidden;
    box-shadow: 0 14px 30px rgba(0,0,0,.45);
  }

  /* Services side */
  .work-gallery {
    position: absolute; left: 18px; right: 18px; top: 18px; height: 150px;
    display: flex; gap: 6px;
  }
  .work-photo { flex: 1; border-radius: 2px; }
  .work-photo--path { background: linear-gradient(180deg, #6f8fb6 0%, #9aa1a8 40%, #55585c 100%); }
  .work-photo--fence { background: linear-gradient(180deg, #5f7a3a 0%, #b39b74 50%, #5e5a55 100%); }
  .work-photo--deck { background: linear-gradient(180deg, #7b8aa0 0%, #b89a6c 45%, #8a6e4a 100%); }
  .work-photo--yard { background: linear-gradient(180deg, #7fa3cf 0%, #a7aaaa 40%, #7c7a74 100%); }

  .services-band {
    position: absolute; left: 0; right: 0; top: 168px; height: 38px;
    background: var(--orange);
    display: flex; align-items: center; justify-content: center;
  }
  .services-title {
    font-family: "Archivo", sans-serif; font-weight: 800;
    font-size: 24px; letter-spacing: 8px; color: #000;
  }
  .services-list {
    position: absolute; left: 0; right: 0; top: 222px;
    text-align: center;
    font-family: "Archivo", sans-serif; font-weight: 400;
    font-size: 17px; line-height: 1.45; color: var(--white);
  }

  /* Contact side */
  .brand {
    position: absolute; left: 0; right: 0; top: 52px;
    display: flex; flex-direction: column; align-items: center;
  }
  .brand-name {
    display: flex; align-items: center; gap: 12px;
    font-family: "Montserrat", sans-serif; font-weight: 800;
    font-size: 46px; letter-spacing: 1px; color: var(--white);
  }
  .brand-mark {
    width: 30px; height: 30px; background: var(--orange);
  }
  .brand-tagline {
    margin-top: 6px;
    font-family: "Montserrat", sans-serif; font-weight: 600;
    font-size: 19px; letter-spacing: 3px; color: var(--white);
  }
  .contact-row {
    position: absolute; left: 30px; right: 24px; top: 196px;
    display: flex; align-items: center; gap: 18px;
  }
  .person { text-align: right; }
  .person-name {
    font-family: "Montserrat", sans-serif; font-weight: 500;
    font-size: 22px; color: var(--orange); white-space: nowrap;
  }
  .person-role {
    font-family: "Montserrat", sans-serif; font-weight: 400;
    font-size: 15px; color: var(--white);
  }
  .divider { width: 2px; height: 56px; background: var(--orange); }
  .contact-list { display: flex; flex-direction: column; gap: 10px; }
  .contact-item {
    display: flex; align-items: center; gap: 8px;
    font-family: "Archivo", sans-serif; font-size: 13.5px; color: var(--grey-text);
    white-space: nowrap;
  }
  .contact-icon { width: 16px; height: 16px; flex: none; }
</style>
</head>
<body>
<main class="sheet">

  <section class="card card--services">
    <div class="work-gallery">
      <div class="work-photo work-photo--path" role="img" aria-label="Photo of a finished paved path beside a building"></div>
      <div class="work-photo work-photo--fence" role="img" aria-label="Photo of a new timber fence and gravel path under a tree"></div>
      <div class="work-photo work-photo--deck" role="img" aria-label="Photo of new timber decking behind a house"></div>
      <div class="work-photo work-photo--yard" role="img" aria-label="Photo of a concrete yard with a small excavator"></div>
    </div>
    <div class="services-band">
      <h2 class="services-title">OUR SERVICES</h2>
    </div>
    <p class="services-list">
      Groundworks / Foundations / Drainage- Landscaping<br>
      / Hard Landscaping / Patios / Decking
    </p>
  </section>

  <section class="card card--contact">
    <div class="brand">
      <div class="brand-name"><span class="brand-mark"></span>TRELLWICK</div>
      <div class="brand-tagline">CONSTRUCTION GROUP LTD</div>
    </div>
    <div class="contact-row">
      <div class="person">
        <div class="person-name">MARCUS HALE</div>
        <div class="person-role">Owner</div>
      </div>
      <div class="divider"></div>
      <div class="contact-list">
        <div class="contact-item">
          <svg class="contact-icon" viewBox="0 0 24 24" aria-hidden="true">
            <path fill="#f0912c" d="M6.6 10.8a15.1 15.1 0 0 0 6.6 6.6l2.2-2.2a1 1 0 0 1 1-.25 11.4 11.4 0 0 0 3.6.57 1 1 0 0 1 1 1V20a1 1 0 0 1-1 1A17 17 0 0 1 3 4a1 1 0 0 1 1-1h3.5a1 1 0 0 1 1 1c0 1.25.2 2.45.57 3.57a1 1 0 0 1-.25 1z"/>
          </svg>
          07931 258 904 / 07713829516
        </div>
        <div class="contact-item">
          <svg class="contact-icon" viewBox="0 0 24 24" aria-hidden="true">
            <rect x="2" y="5" width="20" height="14" rx="1.5" fill="#f0912c"/>
            <path d="M3 6.5l9 6.5 9-6.5" fill="none" stroke="#050505" stroke-width="1.8"/>
          </svg>
          trellgroup@stonevane-mail.com
        </div>
      </div>
    </div>
  </section>

</main>
</body>
</html>
```